Launching a new real estate agency in Monaco

Hello, I am opening a new real estate agency in Monaco. For the purpose of my activity, in order to be known quickly among a fierce competition I need an advertising campaign that will be broadcast in local magazines, newspapers, paper board, etc.

You will find example of pictures of Monaco on which I have the rights and my logo. You can always pick other images that I can buy if the price is reasonable for a commercial use (<200 $)

Please respect the color code.

I wish you good luck and look forward to give you my feedbacks

Reason: Only few projects posted were respecting the brief and of quality. Hoping to receive more in coming days

Target Market(s)

International high-end clientele of all ages, all genders.

Industry/Entity Type

Real Estate Agent

Font styles to use
Serif

Requirements
Must have
• 1/ My logo
• 2/ This message "Un nouveau regard sur l'immobilier" means in English a fresh look at real estate or new eyes on real-estate.
• 3/ My address: 14 rue des Orvilles, Passage Marcellin, 98 000 Monaco
• 4/ Phone number: +377.93.48.25.71
• 5/ Website: www.brunor-agency.com.
• 6/ Format: Files should be easily adjustable but I'd like a vertical display to fit easily in Magazines, Poster and billboard. So please work in high resolution !
Nice to have
• Please think about your design in accordance with the message I want to display.
Should not have
• A simple poster with a picture of Monaco that does not take into consideration the message of the advertisement, "Un nouveau regard sur l'immobilier" which means in english, new eyes on real-estate or a new look at real-estate, or new vision at real-estate.

```html
<!DOCTYPE html>
<html lang="fr">
<head>
<meta charset="UTF-8">
<title>Brunor Agency — Un nouveau regard sur l'immobilier</title>
<link href="https://fonts.googleapis.com/css2?family=Jost:wght@400;500&display=swap" rel="stylesheet">
<style>
  :root {
    --page: #ffffff;
    --brand-red: #c91426;
    --ink-black: #1f1e1f;
    --white: #ffffff;
    --copper: #d49a86;
    --sky-top: #f2b04a;
    --sky-glow: #e2703a;
    --sea: #8c6f9e;
    --sea-deep: #4f4a7e;
    --city-dark: #2a1f24;
  }
  * { margin: 0; padding: 0; box-sizing: border-box; }
  html, body {
    width: 1200px; height: 1200px; overflow: hidden;
    background: var(--page);
    font-family: 'Jost', sans-serif;
  }
  .poster {
    position: absolute;
    left: 218px; top: 61px;
    width: 764px; height: 1080px;
    background: var(--ink-black);
    overflow: hidden;
  }
  .hero-photo {
    position: absolute; left: 0; top: 0;
    width: 764px; height: 510px;
    background:
      radial-gradient(ellipse 60% 40% at 80% 55%, rgba(240,150,60,0.55), transparent 70%),
      linear-gradient(180deg, var(--sky-top) 0%, var(--sky-glow) 14%, var(--sea) 30%, var(--sea-deep) 55%, var(--city-dark) 100%);
  }
  .values-box {
    position: absolute; left: 46px; top: 0;
    width: 187px;
  }
  .values-box__panel {
    background: var(--brand-red);
    height: 150px;
    padding: 28px 0 0 17px;
    color: var(--white);
    font-size: 25px;
    line-height: 33px;
    font-weight: 400;
    letter-spacing: 0.2px;
  }
  .values-box__strip { height: 18px; background: var(--white); }
  .message-band {
    position: absolute; left: 0; top: 510px;
    width: 764px; height: 197px;
    background: var(--brand-red);
    display: flex; align-items: center; justify-content: center;
  }
  .message-band__text {
    color: var(--white);
    font-size: 19px; font-weight: 500;
    letter-spacing: 0.2px;
    margin-top: -12px;
  }
  .contact-block {
    position: absolute; left: 0; top: 707px;
    width: 764px; height: 373px;
    color: var(--white);
    text-align: center;
  }
  .brand {
    position: absolute; top: 112px; left: 0; width: 100%;
    display: flex; align-items: center; justify-content: center; gap: 16px;
  }
  .brand__mark { width: 40px; height: 40px; background: var(--copper); }
  .brand__name {
    color: var(--copper);
    font-size: 38px; font-weight: 500;
    letter-spacing: 3px;
  }
  .address {
    position: absolute; top: 210px; left: 0; width: 100%;
    font-size: 15.5px; line-height: 19.5px; letter-spacing: 0.4px;
  }
  .reach {
    position: absolute; top: 320px; left: 0; width: 100%;
    display: flex; justify-content: center; gap: 26px;
    font-size: 16px; letter-spacing: 0.3px;
  }
  .reach__item { display: flex; align-items: center; gap: 5px; }
  .reach__icon { width: 12px; height: 14px; }
</style>
</head>
<body>
  <main class="poster">
    <div class="hero-photo" role="img" aria-label="Vue aérienne de Monaco au coucher du soleil, côte illuminée et mer violette"></div>

    <div class="values-box">
      <div class="values-box__panel">CONFIANCE<br>ÉTHIQUE<br>QUALITÉ</div>
      <div class="values-box__strip"></div>
    </div>

    <section class="message-band">
      <p class="message-band__text">UN NOUVEAU REGARD SUR L'IMMOBILIER</p>
    </section>

    <section class="contact-block">
      <div class="brand">
        <span class="brand__mark"></span>
        <span class="brand__name">BRUNOR AGENCY</span>
      </div>
      <p class="address">14 rue des Orvilles<br>Passage Marcellin<br>98 000 Monaco</p>
      <div class="reach">
        <span class="reach__item">
          <svg class="reach__icon" viewBox="0 0 12 14"><path d="M4 1 C1 2 1 12 4 13 L5 10 C4 9 4 5 5 4 Z" fill="#fff"/></svg>
          +377.93.48.25.71
        </span>
        <span class="reach__item">
          <svg class="reach__icon" viewBox="0 0 14 14"><circle cx="7" cy="7" r="5.5" fill="none" stroke="#fff" stroke-width="1.2"/><ellipse cx="7" cy="7" rx="2.3" ry="5.5" fill="none" stroke="#fff" stroke-width="1"/><line x1="1.5" y1="7" x2="12.5" y2="7" stroke="#fff" stroke-width="1"/></svg>
          www.brunor-agency.com
        </span>
      </div>
    </section>
  </main>
</body>
</html>
```